Real Estate Brokerage Stationery Designs

I am looking to have presentation folders with business card slots on both sides along with pockets on both sides. I've attached logos, website colors along with current business card designs.

I am looking for envelope designs both big and small. Possibly new business card designs, notepad templates for big and small notepads. Letterhead designs. Pop socket designs. Realtors name badge designs.

www.tallbrookhomes.example

```html
<!DOCTYPE html>
<html lang="en">
<head>
<meta charset="utf-8">
<title>Tallbrook Homes – Envelope</title>
<link href="https://fonts.googleapis.com/css2?family=Lato:wght@400;700&display=swap" rel="stylesheet">
<style>
  :root {
    --navy: #232f66;
    --band-blue: #0b58a6;
    --ring-blue: #1e3f80;
    --ink: #231f20;
    --paper: #ffffff;
    --edge: #1a1a1a;
  }
  html, body {
    margin: 0;
    padding: 0;
    width: 1200px;
    height: 1200px;
    overflow: hidden;
    background: var(--paper);
    font-family: "Lato", sans-serif;
  }
  .envelope {
    position: absolute;
    left: 100px;
    top: 240px;
    width: 1000px;
    height: 647px;
  }
  .envelope-flap {
    position: absolute;
    left: 0;
    top: 0;
  }
  .envelope-body {
    position: absolute;
    left: 0;
    top: 140px;
    width: 1000px;
    height: 507px;
    box-sizing: border-box;
    border: 1.5px solid var(--edge);
    background: var(--paper);
    overflow: hidden;
  }
  .body-art {
    position: absolute;
    left: 0;
    top: 0;
  }
  .brand-name {
    position: absolute;
    left: 113px;
    top: 125px;
    width: 180px;
    text-align: center;
    font-weight: 700;
    font-size: 22px;
    line-height: 1;
    color: var(--ink);
    white-space: nowrap;
  }
  .return-address {
    position: absolute;
    left: 114px;
    top: 245px;
    font-size: 14px;
    color: var(--ink);
    white-space: nowrap;
  }
  .contact-line {
    position: absolute;
    left: 114px;
    top: 270px;
    display: flex;
    align-items: center;
    gap: 8px;
    font-size: 14px;
    color: var(--ink);
    white-space: nowrap;
  }
  .contact-item {
    display: flex;
    align-items: center;
    gap: 4px;
  }
  .contact-icon {
    width: 11px;
    height: 11px;
    fill: var(--band-blue);
    flex: none;
  }
  .web-accent { color: var(--band-blue); }
</style>
</head>
<body>
  <div class="envelope">
    <svg class="envelope-flap" width="1000" height="141" viewBox="0 0 1000 141">
      <polygon role="img" aria-label="Navy flap with a blue diagonal lattice pattern"
               points="63,0 937,0 1000,140 0,140" fill="var(--navy)"/>
    </svg>

    <div class="envelope-body">
      <svg class="body-art" width="1000" height="507" viewBox="0 0 1000 507">
        <rect class="band band-left" x="0" y="68" width="140" height="32" fill="var(--band-blue)"/>
        <rect class="band band-right" x="270" y="184" width="730" height="32" fill="var(--band-blue)"/>
        <circle class="seal-gap" cx="203" cy="139" r="112" fill="var(--paper)"/>
        <circle class="seal-ring" cx="203" cy="139" r="100" fill="none" stroke="var(--ring-blue)" stroke-width="5"/>
      </svg>

      <div class="brand-name">Tallbrook Homes</div>

      <div class="return-address">742 Harbor Point Dr, Suite 310, Lakeview, FL 33000</div>

      <div class="contact-line">
        <span class="contact-item">
          <svg class="contact-icon" viewBox="0 0 12 12"><path d="M3 0h6a1 1 0 0 1 1 1v10a1 1 0 0 1-1 1H3a1 1 0 0 1-1-1V1a1 1 0 0 1 1-1zm0 1.5v8h6v-8z"/></svg>
          <span>555-014-8260</span>
        </span>
        <span class="contact-item">
          <svg class="contact-icon" viewBox="0 0 12 12"><path d="M2.5 0.5l2 2.5-1.2 1.3c.8 1.7 2.2 3.1 3.9 3.9L8.5 7l2.5 2-1.2 2.4C5 11.2.8 7 .6 2.2z"/></svg>
          <span>555-017-3915</span>
        </span>
        <span class="contact-item">
          <svg class="contact-icon" viewBox="0 0 12 12"><path d="M3 0h5v3H3zM1 3.5h10v8H1zm2 2v1h2v-1zm4 0v1h2v-1zm-4 2v1h2v-1zm4 0v1h2v-1z"/></svg>
          <span>555-012-6748</span>
        </span>
        <span class="contact-item">
          <svg class="contact-icon" viewBox="0 0 12 12"><path d="M0 2.5h12v7H0zm1 .8L6 6.6l5-3.3v-.1H1z"/></svg>
          <span>mara@tallbrookhomes.example</span>
        </span>
        <span class="contact-item">
          <svg class="contact-icon" viewBox="0 0 12 12"><circle cx="6" cy="6" r="5" fill="none" stroke="var(--band-blue)" stroke-width="1.2"/><path d="M1 6h10M6 1v10" stroke="var(--band-blue)" stroke-width="1" fill="none"/></svg>
          <span>www.<span class="web-accent">tallbrookhomes</span>.example</span>
        </span>
      </div>
    </div>
  </div>
</body>
</html>
```